Business card design needed

New company in Executive Search & Consulting (Recruitment & Head Hunting Company)

We recruit IT, Accounting & Finance, Human Resources and Senior Management

with offices in Northport, Eastbay, Westmere and South Harbour

Industry/Entity Type

Business

Contact Information for Business Card

Calderwood-Ashfield Executive Search & Consulting
*Northport *Eastbay * Westmere * South Harbour
Neil Calderwood Australian Director
147 Mellor Street Subiaco Western Australia
www.calderwoodashfield.example.au
Ph: 08 6000 4827 Fax: 08 6000 9153
Mobile: 0400 731 562

```html
<!DOCTYPE html>
<html lang="en">
<head>
<meta charset="utf-8">
<title>Calderwood-Ashfield Business Card</title>
<link rel="stylesheet" href="https://fonts.googleapis.com/css2?family=Cinzel:wght@400;500&family=Jost:wght@400&display=swap">
<style>
  :root {
    --backdrop: #bfc0c5;
    --card: #ffffff;
    --ink: #575c67;
    --band: #585e6a;
    --band-text: #ffffff;
    --hairline: #eeeff1;
    --mark: #8d929b;
  }
  * { margin: 0; padding: 0; box-sizing: border-box; }
  html, body {
    width: 1200px;
    height: 1000px;
    overflow: hidden;
    background: var(--backdrop);
  }
  .card {
    position: absolute;
    left: 111px;
    top: 235px;
    width: 978px;
    height: 529px;
    background: var(--card);
  }
  .card__frame {
    position: absolute;
    left: 89px;
    top: 0;
    width: 804px;
    height: 399px;
    border-right: 1px solid var(--hairline);
    border-bottom: 1px solid var(--hairline);
  }
  .brand__mark {
    position: absolute;
    left: 446px;
    top: 58px;
    width: 86px;
    height: 86px;
    background: var(--mark);
  }
  .brand__name {
    position: absolute;
    left: 0;
    width: 100%;
    top: 234px;
    text-align: center;
    font-family: "Cinzel", serif;
    font-weight: 500;
    font-size: 53px;
    line-height: 1;
    letter-spacing: 0.5px;
    color: var(--ink);
  }
  .brand__tagline {
    position: absolute;
    left: 0;
    width: 100%;
    top: 306px;
    text-align: center;
    font-family: "Cinzel", serif;
    font-weight: 500;
    font-size: 30px;
    line-height: 1;
    letter-spacing: 0.3px;
    color: var(--ink);
  }
  .offices {
    position: absolute;
    left: 0;
    width: 100%;
    top: 362px;
    text-align: center;
    font-family: "Jost", sans-serif;
    font-size: 21px;
    line-height: 1;
    letter-spacing: 0.6px;
    color: var(--ink);
  }
  .contact-band {
    position: absolute;
    left: 0;
    bottom: 0;
    width: 100%;
    height: 116px;
    background: var(--band);
    color: var(--band-text);
    font-family: "Jost", sans-serif;
  }
  .person {
    position: absolute;
    left: 0;
    top: 26px;
    width: 240px;
    text-align: center;
  }
  .person__name {
    font-size: 29px;
    line-height: 1.1;
    letter-spacing: 0.3px;
  }
  .person__title {
    margin-top: 4px;
    font-size: 19px;
    line-height: 1.2;
  }
  .details {
    position: absolute;
    left: 280px;
    right: 14px;
    top: 17px;
    text-align: center;
    font-size: 21px;
    line-height: 30px;
    letter-spacing: 0.4px;
  }
  .details__sep {
    display: inline-block;
    width: 3px;
    height: 20px;
    background: var(--band-text);
    vertical-align: -3px;
    margin: 0 3px;
  }
</style>
</head>
<body>
  <section class="card">
    <div class="card__frame"></div>
    <div class="brand__mark"></div>
    <h1 class="brand__name">Calderwood-Ashfield</h1>
    <p class="brand__tagline">EXECUTIVE SEARCH &amp; CONSULTING</p>
    <p class="offices">NORTHPORT &nbsp;|&nbsp; EASTBAY &nbsp;|&nbsp; WESTMERE &nbsp;|&nbsp; SOUTH HARBOUR</p>

    <div class="contact-band">
      <div class="person">
        <p class="person__name">Neil Calderwood</p>
        <p class="person__title">Australian Director</p>
      </div>
      <div class="details">
        <p>147 Mellor Street, Kelmarsh Rise, Eastvale</p>
        <p>www.calderwoodashfield.example.au</p>
        <p>phone 08 6000 4827<span class="details__sep"></span>fax 08 6000 9153<span class="details__sep"></span>mobile 0400 731 562</p>
      </div>
    </div>
  </section>
</body>
</html>
```